Events floral designer business needs a logo design

I need a logo design for my floral design business called tender thorns.
i am inspired by nature and the simplicity of its beauty, whilst upcycling and recycling materials to reduce waste and impact on our environment.
I would like the design to be printed on recycled brown cardboard so i would like a simple but striking design of a bold black ivy vine or gnarly magnolia or tree branch with lower case old school type writer font.

Target Market(s)

Anyone requiring floral additions for their event

Industry/Entity Type

Business

Contact Information for Business Card

mara hollis
floral designer/creator
0418657203
mara@tenderthorns.com
tenderthorns.com

Font styles to use
Other font styles liked:
• lower case type writer

Colors
000000

Requirements
Must have
• simplicity but boldness
• Black typewriter font and bold picture with my details
Nice to have
• as above
Should not have
• colour

```html
<!DOCTYPE html>
<html lang="en">
<head>
<meta charset="utf-8">
<title>Tender Thorns — Business Card</title>
<link href="https://fonts.googleapis.com/css2?family=Didact+Gothic&display=swap" rel="stylesheet">
<style>
  :root {
    --backdrop: #1f1f1f;
    --kraft: #dac8b1;
    --kraft-deep: #cdb497;
    --ink: #141210;
    --ink-soft: #3d352d;
  }
  * { margin: 0; padding: 0; box-sizing: border-box; }
  html, body {
    width: 1189px; height: 1200px; overflow: hidden;
    background: var(--backdrop);
    font-family: "Didact Gothic", "Century Gothic", sans-serif;
    color: var(--ink);
  }
  .canvas { position: relative; width: 1189px; height: 1200px; }
  .card {
    position: absolute; left: 171px; width: 857px; height: 490px;
    background: var(--kraft);
    box-shadow: 0 4px 12px rgba(0,0,0,.55);
    overflow: hidden;
  }
  .card--front { top: 66px; }
  .card--back { top: 625px; }

  .vine-wash {
    position: absolute; border-radius: 50%;
    background: radial-gradient(circle, var(--kraft-deep) 0%, rgba(205,180,151,0) 70%);
  }
  .vine-wash--left { left: -60px; top: -40px; width: 360px; height: 360px; }
  .vine-wash--right { right: -70px; top: 170px; width: 420px; height: 400px; }

  .logo { position: absolute; display: flex; flex-direction: column; align-items: center; }
  .logo__name {
    font-size: 34px; letter-spacing: 5px; color: var(--ink);
    line-height: 1; margin-bottom: 14px; white-space: nowrap;
  }
  .logo__emblem {
    border-radius: 50%;
    border: 3px solid var(--ink);
    background: radial-gradient(circle at 55% 55%, var(--ink-soft) 0%, var(--ink) 75%);
  }
  .card--front .logo { left: 279px; top: 130px; width: 300px; }
  .card--front .logo__emblem { width: 212px; height: 212px; }
  .card--back .logo { left: 83px; top: 115px; width: 300px; }
  .card--back .logo__emblem { width: 204px; height: 204px; }

  .divider {
    position: absolute; left: 425px; top: 138px; width: 1px; height: 216px;
    background: var(--ink);
  }
  .contact { position: absolute; left: 489px; top: 130px; }
  .contact__name { font-size: 30px; font-weight: 700; -webkit-text-stroke: .6px var(--ink); line-height: 1.1; }
  .contact__role { font-size: 23px; margin-top: 6px; letter-spacing: .3px; }
  .contact__list { list-style: none; margin-top: 76px; }
  .contact__item { display: flex; align-items: center; gap: 12px; font-size: 23px; height: 31px; letter-spacing: .4px; }
  .contact__icon { width: 22px; height: 22px; flex: none; }
</style>
</head>
<body>
<main class="canvas">
  <section class="card card--front">
    <div class="vine-wash vine-wash--left" role="img" aria-label="Faint tone-on-tone vine and grape ornament"></div>
    <div class="vine-wash vine-wash--right" role="img" aria-label="Faint tone-on-tone vine and grape ornament"></div>
    <div class="logo">
      <span class="logo__name">tender thorns</span>
      <div class="logo__emblem" role="img" aria-label="Black floral emblem with vines, leaves, grapes and a butterfly inside a ring"></div>
    </div>
  </section>

  <section class="card card--back">
    <div class="logo">
      <span class="logo__name">tender thorns</span>
      <div class="logo__emblem" role="img" aria-label="Black floral emblem with vines, leaves, grapes and a butterfly inside a ring"></div>
    </div>
    <div class="divider"></div>
    <div class="contact">
      <h1 class="contact__name">Mara Hollis</h1>
      <p class="contact__role">Floral designer/creator</p>
      <ul class="contact__list">
        <li class="contact__item">
          <svg class="contact__icon" viewBox="0 0 22 22" aria-hidden="true"><circle cx="11" cy="11" r="10" fill="none" stroke="#141210" stroke-width="2"/><path d="M6 9c0-2 2-3 5-3s5 1 5 3l-2 .5-1-1.5h-4l-1 1.5zM7.5 11h7l1 4h-9z" fill="#141210"/></svg>
          <span>0418657203</span>
        </li>
        <li class="contact__item">
          <svg class="contact__icon" viewBox="0 0 22 22" aria-hidden="true"><circle cx="11" cy="11" r="10" fill="none" stroke="#141210" stroke-width="2"/><rect x="5.5" y="7" width="11" height="8" fill="#141210"/><path d="M5.5 7l5.5 4.5L16.5 7" fill="none" stroke="#dac8b1" stroke-width="1.2"/></svg>
          <span>mara@tenderthorns.com</span>
        </li>
        <li class="contact__item">
          <svg class="contact__icon" viewBox="0 0 22 22" aria-hidden="true"><circle cx="11" cy="11" r="10" fill="none" stroke="#141210" stroke-width="2"/><circle cx="11" cy="11" r="6" fill="#141210"/><path d="M5 11h12M11 5c-2.5 3-2.5 9 0 12M11 5c2.5 3 2.5 9 0 12" fill="none" stroke="#dac8b1" stroke-width="1"/></svg>
          <span>tenderthorns.com</span>
        </li>
      </ul>
    </div>
  </section>
</main>
</body>
</html>
```